BRAVO CONSTRUCTION & RENOVATIONS
BRAVO Construction & Renovations
Project: BRAVO CONSTRUCTION & RENOVATIONS
BRAVO CONSTRUCTION & RENOVATIONS  - Construction
Creative Brief
Professional
Marcus Yelden
Owner
482 Calloway Ln New Braunfels TX
Myelden@bravohomefix.com
www.bravohomefix.com
Exterior and Interior FREE Estimates $0 down 5 star rated

```html
<!DOCTYPE html>
<html lang="en">
<head>
<meta charset="utf-8">
<title>BRAVO Construction & Renovations – Business Cards</title>
<link rel="stylesheet" href="https://fonts.googleapis.com/css2?family=Tinos:ital,wght@0,400;0,700;1,700&family=Montserrat:wght@500&display=swap">
<style>
  :root {
    --stage: #e9e6e1;
    --card: #000000;
    --card-band: #141414;
    --silver: #c9c9c9;
    --text: #d8d8d8;
    --muted: #a9a9a9;
    --green: #2bd92b;
    --rule: #6e6e6e;
  }
  * { margin: 0; padding: 0; box-sizing: border-box; }
  html, body { width: 1200px; height: 713px; overflow: hidden; background: var(--stage); }
  .canvas { position: relative; width: 1200px; height: 713px; }
  .card {
    position: absolute; width: 450px; height: 258px;
    background: var(--card); border-radius: 16px; overflow: hidden;
    font-family: "Tinos", "Times New Roman", serif; color: var(--text);
  }
  .card--front { left: 80px; top: 225px; }
  .card--back { left: 670px; top: 229px; }
  .band {
    position: absolute; left: 0; top: 0; width: 100%; height: 128px;
    background: linear-gradient(180deg, #0a0a0a 0%, var(--card-band) 55%, #050505 100%);
  }
  .brand { position: absolute; left: 0; width: 100%; text-align: center; color: var(--silver); }
  .brand__name { display: block; font-size: 62px; line-height: 1; letter-spacing: 2px; }
  .brand__line { display: block; font-size: 9.5px; letter-spacing: 3.4px; margin-top: 6px; }
  .card--front .brand { top: 40px; }
  .card--back .brand { top: 46px; }
  .phone {
    position: absolute; left: 0; width: 100%; text-align: center;
    font-size: 16px; letter-spacing: 8px; color: var(--text);
  }
  .card--front .phone { top: 137px; }
  .card--back .phone { top: 128px; }
  .offer { position: absolute; top: 166px; width: 100%; text-align: center; font-size: 12px; line-height: 15px; color: var(--text); }
  .offer__free { color: var(--green); font-weight: 700; font-style: italic; }
  .front-web {
    position: absolute; top: 230px; width: 100%; text-align: center;
    font-family: "Montserrat", Arial, sans-serif; font-size: 6.5px; letter-spacing: 1.6px; color: #fff;
  }
  .divider { position: absolute; left: 0; top: 176px; width: 100%; height: 1px; background: var(--rule); }
  .divider__tab { position: absolute; left: 0; top: 172px; width: 122px; height: 5px; background: #9a9a9a; clip-path: polygon(0 0, 94% 0, 100% 100%, 0 100%); }
  .person { position: absolute; left: 16px; top: 188px; }
  .person__name { font-size: 16px; font-weight: 700; color: var(--green); line-height: 18px; }
  .person__role { font-size: 11px; color: var(--muted); }
  .contacts { position: absolute; right: 18px; top: 190px; list-style: none; text-align: right; }
  .contacts li { font-size: 11px; line-height: 16px; color: var(--text); display: flex; justify-content: flex-end; align-items: center; gap: 7px; }
  .contacts svg { width: 11px; height: 11px; flex: none; }
</style>
</head>
<body>
<main class="canvas">
  <section class="card card--front">
    <div class="band"></div>
    <div class="brand">
      <span class="brand__name">BRAVO</span>
      <span class="brand__line">CONSTRUCTION &amp; RENOVATIONS</span>
    </div>
    <p class="phone">830.555.0147</p>
    <p class="offer">Exterior and Interior<br><span class="offer__free">FREE Estimates</span><br>$0 down 5 star rated</p>
    <p class="front-web">www.bravohomefix.com</p>
  </section>

  <section class="card card--back">
    <div class="brand">
      <span class="brand__name">BRAVO</span>
      <span class="brand__line">CONSTRUCTION &amp; RENOVATIONS</span>
    </div>
    <p class="phone">830.555.0147</p>
    <div class="divider"></div>
    <div class="divider__tab"></div>
    <div class="person">
      <p class="person__name">Marcus Yelden</p>
      <p class="person__role">Owner</p>
    </div>
    <ul class="contacts">
      <li>482 Calloway Ln, New Braunfels TX
        <svg viewBox="0 0 12 12"><path d="M6 1a3.5 3.5 0 0 0-3.5 3.5C2.5 7 6 10.5 6 10.5S9.5 7 9.5 4.5A3.5 3.5 0 0 0 6 1z" fill="var(--green)"/><circle cx="6" cy="4.5" r="1.3" fill="#000"/></svg></li>
      <li>Myelden@bravohomefix.com
        <svg viewBox="0 0 12 12"><rect x="1" y="2.5" width="10" height="7" fill="var(--green)"/><path d="M1 2.5l5 4 5-4" stroke="#000" fill="none"/></svg></li>
      <li>www.bravohomefix.com
        <svg viewBox="0 0 12 12" fill="none" stroke="var(--green)" stroke-width="1"><circle cx="6" cy="6" r="4.8"/><ellipse cx="6" cy="6" rx="2" ry="4.8"/><path d="M1.2 6h9.6M2 3.5h8M2 8.5h8"/></svg></li>
    </ul>
  </section>
</main>
</body>
</html>
```